依頼詳細
サイズ:[長形3号]・[角形2号]
でお願いします。

注1:ロゴデータは、アルファベット『RINWA』がメインです。
漢字のパターンも一応添付させて頂きますので、必要であればお使いください。
記載項目
【封筒】

社名:株式会社 凛和
(英字表記:RINWA)

住所:〒111-1111
大阪市××××××××××××××

TEL:00-0000-0000
FAX:00-0000-0000

以上になります。
半角・全角・ハイフン有無等は、調整して頂いて結構です。
希望イメージ
シンプル 複雑
単色 カラフル
暗い 明るい
日常 高級
遊び心 厳粛
未来的 伝統的
女性的 男性的
希望する色
納品ファイル
• 高解像度JPG (.jpg)
• イラストレーター形式 (.ai)
• PNG形式 (.png)
補足説明

いいデザインに気に入ってます。

ありがとうございます。

```html
<!DOCTYPE html>
<html lang="ja">
<head>
<meta charset="utf-8">
<title>RINWA 封筒 角形2号</title>
<link href="https://fonts.googleapis.com/css2?family=Michroma&family=Noto+Sans+JP:wght@400;500&display=swap" rel="stylesheet">
<style>
  :root {
    --backdrop: #d9d9d9;
    --paper: #ffffff;
    --brand-red: #d7000f;
    --flap-red: #d10010;
    --ink: #d7000f;
    --shadow: rgba(0,0,0,0.18);
  }
  html, body {
    margin: 0;
    width: 846px;
    height: 1200px;
    overflow: hidden;
    background: var(--backdrop);
  }
  .envelope {
    position: absolute;
    left: 141px;
    top: 79px;
    width: 566px;
    height: 1043px;
    background: var(--paper);
    box-shadow: 0 2px 8px var(--shadow);
  }
  .envelope__flap {
    position: absolute;
    left: 0;
    top: 0;
    width: 100%;
    height: 96px;
  }
  .envelope__flap-mark {
    position: absolute;
    right: 40px;
    top: 30px;
    font-family: "Michroma", sans-serif;
    font-size: 13px;
    letter-spacing: 2px;
    color: var(--paper);
  }
  .envelope__panel {
    position: absolute;
    left: 80px;
    top: 113px;
    right: 12px;
    height: 671px;
    background: var(--brand-red);
    border-radius: 14px 0 0 0;
  }
  .envelope__wordmark {
    position: absolute;
    left: 22px;
    top: 130px;
    width: 48px;
    height: 770px;
    display: flex;
    align-items: center;
    justify-content: center;
  }
  .envelope__wordmark span {
    display: block;
    transform: rotate(90deg);
    white-space: nowrap;
    font-family: "Michroma", sans-serif;
    font-size: 58px;
    letter-spacing: 26px;
    color: var(--ink);
  }
  .sender {
    position: absolute;
    left: 340px;
    top: 818px;
    width: 210px;
    color: var(--ink);
  }
  .sender__brand {
    display: flex;
    align-items: center;
    gap: 10px;
  }
  .sender__dot {
    width: 22px;
    height: 22px;
    border-radius: 50%;
    background: var(--ink);
  }
  .sender__name-en {
    font-family: "Michroma", sans-serif;
    font-size: 26px;
    letter-spacing: 1px;
  }
  .sender__name-ja {
    margin: 4px 0 0 80px;
    font-family: "Noto Sans JP", sans-serif;
    font-size: 12px;
    font-weight: 500;
  }
  .sender__address {
    position: absolute;
    left: 98px;
    top: 1040px;
    right: 22px;
    font-family: "Noto Sans JP", sans-serif;
    font-size: 10.5px;
    line-height: 20px;
    color: var(--ink);
  }
  .sender__address p { margin: 0; }
  .sender__address .contact span + span { margin-left: 14px; }
</style>
</head>
<body>
  <div class="envelope">
    <svg class="envelope__flap" viewBox="0 0 566 96" preserveAspectRatio="none" aria-hidden="true">
      <rect x="0" y="0" width="566" height="96" fill="var(--flap-red)"/>
    </svg>
    <div class="envelope__flap-mark">RINWA</div>

    <div class="envelope__panel"></div>

    <div class="envelope__wordmark"><span>RINWA</span></div>

    <div class="sender">
      <div class="sender__brand">
        <div class="sender__dot"></div>
        <div class="sender__name-en">RINWA</div>
      </div>
      <div class="sender__name-ja">株式会社 凛和</div>
    </div>

    <div class="sender__address" style="left:340px;top:888px;right:auto;width:230px;position:absolute;">
      <p>〒111-1111 大阪市××××××××××</p>
      <p class="contact"><span>TEL.00-0000-0000</span><span>FAX.00-0000-0000</span></p>
    </div>
  </div>
</body>
</html>
```